Kinesiology undergraduate program needs an infographic

We would like an infographic to creatively and succinctly inform students, faculty, staff, and others about our undergraduate values and competencies (perhaps also integrating our mission and vision). We would like to see a design that incorporates the definition of Kinesiology (the study of human movement) and the colors of our Westbrook State University at Larkfield.

```html
<!DOCTYPE html>
<html lang="en">
<head>
<meta charset="utf-8">
<title>Kinesiology Undergraduate Program – Competencies Infographic</title>
<link href="https://fonts.googleapis.com/css2?family=Montserrat:wght@500;600;700;800&family=Open+Sans:wght@400;600;700&display=swap" rel="stylesheet">
<style>
:root{
  --navy:#0b2d6b;
  --red:#d50032;
  --teal:#16917f;
  --teal-dark:#0c5f73;
  --ink:#27313f;
  --muted:#7a8390;
  --rule:#d7dce3;
  --page:#eceef2;
  --white:#ffffff;
}
*{box-sizing:border-box;margin:0;padding:0}
html,body{width:1200px;height:3012px;overflow:hidden;background:var(--page)}
body{font-family:"Open Sans",Arial,sans-serif;color:var(--ink);padding:20px}
.board{width:1160px;height:977px;background:var(--white);display:flex;box-shadow:0 2px 10px rgba(0,0,0,.12);margin-bottom:20px;position:relative}
.board:last-child{margin-bottom:0}

/* sidebar */
.sidebar{width:250px;flex:none;display:flex;flex-direction:column}
.institution-name{height:170px;padding:34px 26px;font-family:"Open Sans",Arial,sans-serif;font-weight:600;font-size:16px;line-height:1.35;color:var(--ink)}
.statements{flex:1;background:var(--navy);color:var(--white);padding:34px 24px;display:flex;flex-direction:column;justify-content:space-around}
.statement-head{display:flex;align-items:center;gap:10px;margin-bottom:10px}
.statement-icon{width:40px;height:40px;flex:none}
.statement h3{font-family:"Montserrat",Arial,sans-serif;font-size:17px;font-weight:800;text-transform:uppercase;letter-spacing:.5px}
.statement p{font-size:16px;line-height:1.4;font-weight:600}

/* main */
.main{flex:1;position:relative;padding:34px 36px 60px}
.intro{font-size:13px;line-height:1.55;color:var(--muted);max-width:800px}
.intro strong{color:var(--ink)}
.program-footer{position:absolute;right:30px;bottom:22px;font-family:"Open Sans",Arial,sans-serif;font-weight:600;font-size:15px;color:var(--muted)}

.comp-list{list-style:none;font-size:15px;line-height:1.65;font-weight:600;color:var(--ink)}
.comp-list li{padding-left:14px;position:relative}
.comp-list li::before{content:"";position:absolute;left:0;top:10px;width:6px;height:6px;border-radius:50%;background:currentColor;opacity:.55}

/* variant 1: wheel */
.wheel-stage{position:absolute;left:36px;right:36px;top:150px;bottom:60px}
.wheel{position:absolute;left:50%;top:50%;width:520px;height:520px;transform:translate(-50%,-50%)}
.wheel-label{font-family:"Montserrat",Arial,sans-serif;font-weight:800;font-size:14px;fill:var(--white);letter-spacing:1px;text-transform:uppercase}
.wheel-center{font-family:"Montserrat",Arial,sans-serif;font-weight:700;font-size:21px;fill:var(--navy)}
.wheel-list{position:absolute;width:220px;padding-top:12px;border-top:2px dotted var(--rule)}
.wheel-list.tl{left:0;top:70px}
.wheel-list.tr{right:0;top:70px}
.wheel-list.bl{left:0;bottom:70px}
.wheel-list.br{right:0;bottom:70px}

/* variant 2: hub and boxes */
.hub-stage{position:absolute;left:36px;right:36px;top:150px;bottom:60px}
.hub-lines{position:absolute;inset:0;width:100%;height:100%}
.hub{position:absolute;left:50%;top:50%;width:230px;height:230px;margin:-115px 0 0 -115px;border-radius:50%;border:6px solid var(--navy);background:var(--white);display:flex;align-items:center;justify-content:center;text-align:center;font-family:"Montserrat",Arial,sans-serif;font-weight:700;font-size:20px;line-height:1.3;color:var(--navy);padding:18px}
.comp-box{position:absolute;width:290px;background:var(--white);border:1px solid var(--rule);box-shadow:0 2px 6px rgba(0,0,0,.08)}
.comp-box h4{font-family:"Montserrat",Arial,sans-serif;font-weight:800;font-size:16px;text-transform:uppercase;color:var(--white);padding:12px 16px;line-height:1.25}
.comp-box .comp-list{padding:14px 18px 18px}
.comp-box.tl{left:0;top:20px}.comp-box.tr{right:0;top:20px}
.comp-box.bl{left:0;bottom:20px}.comp-box.br{right:0;bottom:20px}
.bg-teal{background:var(--teal)}.bg-red{background:var(--red)}.bg-navy{background:var(--navy)}.bg-tealdark{background:var(--teal-dark)}

/* variant 3: grid */
.grid-band{margin-top:34px;background:linear-gradient(90deg,var(--teal-dark),var(--teal));color:var(--white);font-family:"Montserrat",Arial,sans-serif;font-weight:800;font-size:24px;letter-spacing:1px;text-transform:uppercase;padding:20px 30px;text-align:center}
.comp-grid{display:grid;grid-template-columns:1fr 1fr;margin-top:34px;border-top:1px solid var(--rule)}
.comp-cell{display:flex;gap:20px;padding:34px 22px;border-bottom:1px solid var(--rule)}
.comp-cell:nth-child(odd){border-right:1px solid var(--rule)}
.cell-icon{width:64px;height:64px;flex:none;display:flex;align-items:center;justify-content:center}
.comp-cell h4{font-family:"Montserrat",Arial,sans-serif;font-weight:800;font-size:21px;line-height:1.2;text-transform:uppercase;margin-bottom:10px}
.t-teal{color:var(--teal)}.t-red{color:var(--red)}.t-navy{color:var(--navy)}.t-tealdark{color:var(--teal-dark)}
</style>
</head>
<body>

<!-- ===== Variant 1: competency wheel ===== -->
<section class="board">
  <aside class="sidebar">
    <div class="institution-name">Westbrook State University at Larkfield</div>
    <div class="statements">
      <div class="statement">
        <div class="statement-head">
          <svg class="statement-icon" viewBox="0 0 40 40"><circle cx="20" cy="20" r="18" fill="none" stroke="#fff" stroke-width="2"/><circle cx="20" cy="20" r="10" fill="none" stroke="#fff" stroke-width="2"/><circle cx="20" cy="20" r="3" fill="#fff"/></svg>
          <h3>Our Mission</h3>
        </div>
        <p>To empower undergraduate students to pursue excellence through scientific discovery, clinical practice, and health promotion</p>
      </div>
      <div class="statement">
        <div class="statement-head">
          <svg class="statement-icon" viewBox="0 0 40 40"><circle cx="20" cy="20" r="18" fill="none" stroke="#fff" stroke-width="2"/><path d="M8 20c4-6 20-6 24 0-4 6-20 6-24 0z" fill="none" stroke="#fff" stroke-width="2"/><circle cx="20" cy="20" r="3.5" fill="#fff"/></svg>
          <h3>Our Vision</h3>
        </div>
        <p>WSU Kinesiology graduates are leaders who excel in careers that enhance the quality of life of individuals and communities</p>
      </div>
      <div class="statement">
        <div class="statement-head">
          <svg class="statement-icon" viewBox="0 0 40 40"><circle cx="20" cy="20" r="18" fill="none" stroke="#fff" stroke-width="2"/><path d="M20 9l3.2 7 7.3.7-5.5 5 1.6 7.3L20 25.3 13.4 29l1.6-7.3-5.5-5 7.3-.7z" fill="#fff"/></svg>
          <h3>Our Values</h3>
        </div>
        <p>Student Success, Science and Service</p>
      </div>
    </div>
  </aside>
  <div class="main">
    <p class="intro"><strong>Lorem Ipsum</strong> is simply dummy text of the printing and typesetting industry. Lorem Ipsum has been the industry's standard dummy text ever since the 1500s, when an unknown printer took a galley of type and scrambled it to make a type specimen book.</p>
    <div class="wheel-stage">
      <ul class="comp-list wheel-list tl"><li>Cultural Humility/Sensitivity</li><li>Integrity</li><li>Self Directed</li><li>Dependability</li><li>Mission Oriented</li></ul>
      <ul class="comp-list wheel-list tr"><li>Foundational Concepts of Kinesiology</li><li>Clinical Application</li><li>Scientific Communication</li></ul>
      <ul class="comp-list wheel-list bl"><li>Cultural Competence</li><li>Professionalism</li><li>Leadership and Teamwork</li><li>Service Orientation/Citizenship</li></ul>
      <ul class="comp-list wheel-list br"><li>Critical Thinking</li><li>Quantitative Reasoning</li><li>Scientific Inquiry</li><li>Concept Integration</li></ul>
      <svg class="wheel" viewBox="170 60 520 520">
        <defs>
          <path id="arc-tl-1" d="M234,320 A196,196 0 0 1 430,124"/>
          <path id="arc-tl-2" d="M260,320 A170,170 0 0 1 430,150"/>
          <path id="arc-tr-1" d="M430,124 A196,196 0 0 1 626,320"/>
          <path id="arc-tr-2" d="M430,150 A170,170 0 0 1 600,320"/>
          <path id="arc-bl-1" d="M258,320 A172,172 0 0 0 430,492"/>
          <path id="arc-bl-2" d="M232,320 A198,198 0 0 0 430,518"/>
          <path id="arc-br-1" d="M430,492 A172,172 0 0 0 602,320"/>
          <path id="arc-br-2" d="M430,518 A198,198 0 0 0 628,320"/>
        </defs>
        <path d="M200.1,312 A230,230 0 0 1 422,90.1 L425.1,180.1 A140,140 0 0 0 290.1,315.1 Z" fill="var(--teal)"/>
        <path d="M438,90.1 A230,230 0 0 1 659.9,312 L569.9,315.1 A140,140 0 0 0 434.9,180.1 Z" fill="var(--red)"/>
        <path d="M659.9,328 A230,230 0 0 1 438,549.9 L434.9,459.9 A140,140 0 0 0 569.9,324.9 Z" fill="var(--teal-dark)"/>
        <path d="M422,549.9 A230,230 0 0 1 200.1,328 L290.1,324.9 A140,140 0 0 0 425.1,459.9 Z" fill="var(--navy)"/>
        <text class="wheel-label"><textPath href="#arc-tl-1" startOffset="50%" text-anchor="middle">Intrapersonal</textPath></text>
        <text class="wheel-label"><textPath href="#arc-tl-2" startOffset="50%" text-anchor="middle">Growth</textPath></text>
        <text class="wheel-label"><textPath href="#arc-tr-1" startOffset="50%" text-anchor="middle">The Science of</textPath></text>
        <text class="wheel-label"><textPath href="#arc-tr-2" startOffset="50%" text-anchor="middle">Kinesiology</textPath></text>
        <text class="wheel-label"><textPath href="#arc-bl-1" startOffset="50%" text-anchor="middle">Relationships and</textPath></text>
        <text class="wheel-label"><textPath href="#arc-bl-2" startOffset="50%" text-anchor="middle">Communication</textPath></text>
        <text class="wheel-label"><textPath href="#arc-br-1" startOffset="50%" text-anchor="middle">Thinking and</textPath></text>
        <text class="wheel-label"><textPath href="#arc-br-2" startOffset="50%" text-anchor="middle">Reasoning</textPath></text>
        <circle cx="430" cy="320" r="126" fill="#fff" stroke="var(--navy)" stroke-width="4"/>
        <text class="wheel-center" x="430" y="300" text-anchor="middle">Our Graduates</text>
        <text class="wheel-center" x="430" y="328" text-anchor="middle">Will Be</text>
        <text class="wheel-center" x="430" y="356" text-anchor="middle">Competent In...</text>
      </svg>
    </div>
    <div class="program-footer">WSU Health</div>
  </div>
</section>

<!-- ===== Variant 2: hub with boxes ===== -->
<section class="board">
  <aside class="sidebar">
    <div class="institution-name">Westbrook State University at Larkfield</div>
    <div class="statements">
      <div class="statement">
        <div class="statement-head">
          <svg class="statement-icon" viewBox="0 0 40 40"><circle cx="20" cy="20" r="18" fill="none" stroke="#fff" stroke-width="2"/><circle cx="20" cy="20" r="10" fill="none" stroke="#fff" stroke-width="2"/><circle cx="20" cy="20" r="3" fill="#fff"/></svg>
          <h3>Our Mission</h3>
        </div>
        <p>To empower undergraduate students to pursue excellence through scientific discovery, clinical practice, and health promotion</p>
      </div>
      <div class="statement">
        <div class="statement-head">
          <svg class="statement-icon" viewBox="0 0 40 40"><circle cx="20" cy="20" r="18" fill="none" stroke="#fff" stroke-width="2"/><path d="M8 20c4-6 20-6 24 0-4 6-20 6-24 0z" fill="none" stroke="#fff" stroke-width="2"/><circle cx="20" cy="20" r="3.5" fill="#fff"/></svg>
          <h3>Our Vision</h3>
        </div>
        <p>WSU Kinesiology graduates are leaders who excel in careers that enhance the quality of life of individuals and communities</p>
      </div>
      <div class="statement">
        <div class="statement-head">
          <svg class="statement-icon" viewBox="0 0 40 40"><circle cx="20" cy="20" r="18" fill="none" stroke="#fff" stroke-width="2"/><path d="M20 9l3.2 7 7.3.7-5.5 5 1.6 7.3L20 25.3 13.4 29l1.6-7.3-5.5-5 7.3-.7z" fill="#fff"/></svg>
          <h3>Our Values</h3>
        </div>
        <p>Student Success, Science and Service</p>
      </div>
    </div>
  </aside>
  <div class="main">
    <p class="intro"><strong>Lorem Ipsum</strong> is simply dummy text of the printing and typesetting industry. Lorem Ipsum has been the industry's standard dummy text ever since the 1500s, when an unknown printer took a galley of type and scrambled it to make a type specimen book.</p>
    <div class="hub-stage">
      <svg class="hub-lines" viewBox="0 0 838 767" preserveAspectRatio="none">
        <path d="M290 130 H360 V300" fill="none" stroke="var(--teal)" stroke-width="3"/>
        <path d="M548 130 H478 V300" fill="none" stroke="var(--red)" stroke-width="3"/>
        <path d="M290 637 H360 V467" fill="none" stroke="var(--navy)" stroke-width="3"/>
        <path d="M548 637 H478 V467" fill="none" stroke="var(--teal-dark)" stroke-width="3"/>
      </svg>
      <div class="comp-box tl"><h4 class="bg-teal">Intrapersonal Growth</h4><ul class="comp-list"><li>Cultural Humility/Sensitivity</li><li>Integrity</li><li>Self Directed</li><li>Dependability</li><li>Mission Oriented</li></ul></div>
      <div class="comp-box tr"><h4 class="bg-red">The Science of Kinesiology</h4><ul class="comp-list"><li>Cultural Humility/Sensitivity</li><li>Integrity</li><li>Self Directed</li><li>Dependability</li><li>Mission Oriented</li></ul></div>
      <div class="comp-box bl"><h4 class="bg-navy">Relationships and Communication</h4><ul class="comp-list"><li>Cultural Competence</li><li>Professionalism</li><li>Leadership and Teamwork</li><li>Service Orientation/Citizenship</li></ul></div>
      <div class="comp-box br"><h4 class="bg-tealdark">Thinking and Reasoning</h4><ul class="comp-list"><li>Critical Thinking</li><li>Quantitative Reasoning</li><li>Scientific Inquiry</li><li>Concept Integration</li></ul></div>
      <div class="hub">Our Graduates Will Be Competent In...</div>
    </div>
    <div class="program-footer">WSU Health</div>
  </div>
</section>

<!-- ===== Variant 3: grid ===== -->
<section class="board">
  <aside class="sidebar">
    <div class="institution-name">Westbrook State University at Larkfield</div>
    <div class="statements">
      <div class="statement">
        <div class="statement-head">
          <svg class="statement-icon" viewBox="0 0 40 40"><circle cx="20" cy="20" r="18" fill="none" stroke="#fff" stroke-width="2"/><circle cx="20" cy="20" r="10" fill="none" stroke="#fff" stroke-width="2"/><circle cx="20" cy="20" r="3" fill="#fff"/></svg>
          <h3>Our Mission</h3>
        </div>
        <p>To empower undergraduate students to pursue excellence through scientific discovery, clinical practice, and health promotion</p>
      </div>
      <div class="statement">
        <div class="statement-head">
          <svg class="statement-icon" viewBox="0 0 40 40"><circle cx="20" cy="20" r="18" fill="none" stroke="#fff" stroke-width="2"/><path d="M8 20c4-6 20-6 24 0-4 6-20 6-24 0z" fill="none" stroke="#fff" stroke-width="2"/><circle cx="20" cy="20" r="3.5" fill="#fff"/></svg>
          <h3>Our Vision</h3>
        </div>
        <p>WSU Kinesiology graduates are leaders who excel in careers that enhance the quality of life of individuals and communities</p>
      </div>
      <div class="statement">
        <div class="statement-head">
          <svg class="statement-icon" viewBox="0 0 40 40"><circle cx="20" cy="20" r="18" fill="none" stroke="#fff" stroke-width="2"/><path d="M20 9l3.2 7 7.3.7-5.5 5 1.6 7.3L20 25.3 13.4 29l1.6-7.3-5.5-5 7.3-.7z" fill="#fff"/></svg>
          <h3>Our Values</h3>
        </div>
        <p>Student Success, Science and Service</p>
      </div>
    </div>
  </aside>
  <div class="main">
    <p class="intro"><strong>Lorem Ipsum</strong> is simply dummy text of the printing and typesetting industry. Lorem Ipsum has been the industry's standard dummy text ever since the 1500s, when an unknown printer took a galley of type and scrambled it to make a type specimen book.</p>
    <div class="grid-band">Our Graduates Will Be Competent In...</div>
    <div class="comp-grid">
      <div class="comp-cell">
        <div class="cell-icon bg-teal"><svg width="36" height="36" viewBox="0 0 36 36"><circle cx="18" cy="11" r="6" fill="none" stroke="#fff" stroke-width="2.5"/><path d="M7 31c1-7 5-10 11-10s10 3 11 10" fill="none" stroke="#fff" stroke-width="2.5"/></svg></div>
        <div><h4 class="t-teal">Intrapersonal Growth</h4><ul class="comp-list"><li>Cultural Humility/Sensitivity</li><li>Integrity</li><li>Self Directed</li><li>Dependability</li><li>Mission Oriented</li></ul></div>
      </div>
      <div class="comp-cell">
        <div class="cell-icon bg-red"><svg width="36" height="36" viewBox="0 0 36 36"><path d="M4 19h7l3-8 5 16 4-11 2 3h7" fill="none" stroke="#fff" stroke-width="2.5" stroke-linejoin="round"/></svg></div>
        <div><h4 class="t-red">The Science of Kinesiology</h4><ul class="comp-list"><li>Cultural Humility/Sensitivity</li><li>Integrity</li><li>Self Directed</li><li>Dependability</li><li>Mission Oriented</li></ul></div>
      </div>
      <div class="comp-cell">
        <div class="cell-icon bg-navy"><svg width="36" height="36" viewBox="0 0 36 36"><rect x="4" y="7" width="18" height="12" rx="2" fill="none" stroke="#fff" stroke-width="2.5"/><rect x="14" y="17" width="18" height="12" rx="2" fill="none" stroke="#fff" stroke-width="2.5"/></svg></div>
        <div><h4 class="t-navy">Relationships and Communication</h4><ul class="comp-list"><li>Cultural Competence</li><li>Professionalism</li><li>Leadership and Teamwork</li><li>Service Orientation/Citizenship</li></ul></div>
      </div>
      <div class="comp-cell">
        <div class="cell-icon bg-tealdark"><svg width="36" height="36" viewBox="0 0 36 36"><path d="M18 5a9 9 0 0 0-5 16.5V26h10v-4.5A9 9 0 0 0 18 5z" fill="none" stroke="#fff" stroke-width="2.5"/><path d="M14 31h8" stroke="#fff" stroke-width="2.5"/></svg></div>
        <div><h4 class="t-tealdark">Thinking and Reasoning</h4><ul class="comp-list"><li>Critical Thinking</li><li>Quantitative Reasoning</li><li>Scientific Inquiry</li><li>Concept Integration</li></ul></div>
      </div>
    </div>
    <div class="program-footer">WSU Health</div>
  </div>
</section>

</body>
</html>
```